Morvex Business Card (intended for Business Card sized magnet)

Hi guys,

I would like to get a design for my business card for the restaurant. The design must be single sided as I intend to produce business card sized magnets.

The File attached must me on and I'm open for new ides

Can you please ensure that the design meets Cardowell's magnetic business card size specifications:

http://www.cardowell.example.au/custom-magnets.aspx?txi=15695&xnid=TopNav_Magnetic+Business+Cards+(linked+item)_Magnets_Marketing+Products&xnav=TopNav

Full Bleed Size (starting document size):
90 x 52 mm
1062 x 615 pixels
* Finished artwork should use the full bleed dimensions for best results.

Document Trim Size (final size after being cut):
87 x 49 mm
1028 x 579 pixels
* Please be sure to keep all text within the safe margin.

Resolution:
300 DPI

The winning design/source files need to meet these specifications.

Thanks
Updates

Hi guys, can I see more options please Thanks

```html
<!DOCTYPE html>
<html lang="en">
<head>
<meta charset="utf-8">
<title>Morvex Business Card</title>
<link rel="stylesheet" href="https://fonts.googleapis.com/css2?family=Crimson+Pro:wght@400;700&family=Pinyon+Script&display=swap">
<style>
  :root {
    --page: #ffffff;
    --card-black: #000000;
    --card-blue: #1f3fd6;
    --card-blue-deep: #0a1a7a;
    --ink-white: #ffffff;
    --script-grey: #8c8c8c;
    --badge: #050505;
  }
  html, body {
    margin: 0;
    padding: 0;
    width: 1200px;
    height: 1000px;
    overflow: hidden;
    background: var(--page);
  }
  .business-card {
    position: absolute;
    left: 231px;
    top: 286px;
    width: 731px;
    height: 423px;
    overflow: hidden;
    background:
      radial-gradient(ellipse 70% 85% at 78% 50%, var(--card-blue) 0%, #1530b8 45%, var(--card-blue-deep) 80%, transparent 100%),
      linear-gradient(90deg, var(--card-black) 0%, var(--card-black) 38%, var(--card-blue-deep) 60%, var(--card-blue-deep) 100%);
  }
  .food-photo {
    position: absolute;
    left: 52px;
    top: 30px;
    width: 340px;
    height: 312px;
    border-radius: 50%;
    background: radial-gradient(circle at 50% 50%, #c9862f 0%, #a8703a 30%, #6b5434 55%, rgba(40,30,20,0.6) 75%, transparent 100%);
  }
  .tagline {
    position: absolute;
    font-family: "Pinyon Script", cursive;
    color: var(--script-grey);
    margin: 0;
    white-space: nowrap;
    line-height: 1;
  }
  .tagline-top { left: 50px; top: 308px; font-size: 44px; }
  .tagline-bottom { left: 66px; top: 360px; font-size: 30px; }
  .brand-name {
    position: absolute;
    left: 452px;
    top: 28px;
    margin: 0;
    font-family: "Crimson Pro", serif;
    font-weight: 400;
    font-size: 86px;
    line-height: 1;
    color: var(--ink-white);
    letter-spacing: 1px;
  }
  .rule {
    position: absolute;
    left: 447px;
    width: 242px;
    height: 3px;
    background: var(--ink-white);
  }
  .rule-top { top: 122px; }
  .rule-bottom { top: 202px; }
  .ornament-band {
    position: absolute;
    left: 447px;
    top: 131px;
    width: 242px;
    height: 65px;
    background: linear-gradient(90deg, #2a49d8, #3d5ae0, #2a49d8);
  }
  .contact-list {
    position: absolute;
    left: 446px;
    top: 218px;
    margin: 0;
    padding: 0;
    list-style: none;
    font-family: "Crimson Pro", serif;
    font-size: 23px;
    line-height: 27.5px;
    color: var(--ink-white);
  }
  .contact-list li {
    position: relative;
    padding-left: 26px;
  }
  .contact-badge {
    position: absolute;
    left: 0;
    top: 4px;
    width: 19px;
    height: 19px;
    border-radius: 50%;
    background: var(--badge);
    border: 1px solid #cfd6ff;
    box-sizing: border-box;
    color: var(--ink-white);
    font-size: 14px;
    line-height: 16px;
    text-align: center;
  }
  .call-line {
    position: absolute;
    left: 419px;
    top: 358px;
    margin: 0;
    font-family: "Crimson Pro", serif;
    font-weight: 700;
    font-size: 29px;
    line-height: 1;
    color: var(--ink-white);
    white-space: nowrap;
  }
</style>
</head>
<body>
  <section class="business-card">
    <div class="food-photo" role="img" aria-label="Photograph of six Middle Eastern mezze dishes arranged in a flower shape around a central bowl of dips"></div>

    <p class="tagline tagline-top">Authentic</p>
    <p class="tagline tagline-bottom">Middle Eastern Cuisine</p>

    <h1 class="brand-name">Morvex</h1>
    <div class="rule rule-top"></div>
    <div class="ornament-band" role="img" aria-label="Decorative geometric star pattern band with red, green and yellow accents"></div>
    <div class="rule rule-bottom"></div>

    <ul class="contact-list">
      <li><span class="contact-badge">a</span>214 Ferncroft Rd,<br>Ashvale North, 3190</li>
      <li><span class="contact-badge">w</span>www.morvex.example.au</li>
      <li><span class="contact-badge"></span>morvexkitchen</li>
    </ul>

    <p class="call-line">Call us: 03 9000 4127</p>
  </section>
</body>
</html>
```